Industrial Company-Pop-Up Banner Design for Demolition and Infrastructure Company

Hi-
We need to create 2 pop-up banners for our company. They will both have the same logo, but different photos. We would like to have the colors white, red, and black and feature a modern design. I have attached some inspiration photos.

Target Market(s)

Trade Show/Job Fair Audience

Industry/Entity Type

construction, industrial

Font styles to use
Sans Serif

Colors
EB3D1F
EC4F4E
F09395
F8D3D4
FCEDEE

Requirements
Must have
• 2 versions, each with different photos but same design. Logo, Red, Black, and White Color Scheme, Modern Design
Nice to have
• Modern Design similar to the inspiration photos

```html
<!DOCTYPE html>
<html lang="en">
<head>
<meta charset="utf-8">
<title>R.T. Hollister Companies – Pop-Up Banners</title>
<link rel="stylesheet" href="https://fonts.googleapis.com/css2?family=Kaushan+Script&family=Poppins:wght@500;600;700&display=swap">
<style>
  :root {
    --page-bg: #e4e4e6;
    --brand-red: #e0232b;
    --ink: #111111;
    --header-black: #1b1b1b;
    --white: #ffffff;
  }
  html, body {
    margin: 0;
    padding: 0;
    width: 800px;
    height: 1200px;
    overflow: hidden;
    background: var(--page-bg);
  }
  .canvas {
    position: relative;
    width: 800px;
    height: 1200px;
    display: flex;
    justify-content: center;
    align-items: center;
    gap: 30px;
  }
  .banner {
    width: 340px;
    height: 816px;
    display: block;
    box-shadow: 0 10px 28px rgba(0,0,0,0.22);
  }
  .tagline-top {
    font-family: "Poppins", sans-serif;
    font-weight: 700;
    font-size: 24px;
    fill: var(--white);
  }
  .tagline-script {
    font-family: "Kaushan Script", cursive;
    font-size: 96px;
    fill: var(--brand-red);
    stroke: var(--brand-red);
    stroke-width: 1.5px;
  }
  .since-text {
    font-family: "Poppins", sans-serif;
    font-weight: 500;
    font-size: 24px;
    fill: var(--ink);
  }
  .brand-name {
    font-family: "Poppins", sans-serif;
    font-weight: 700;
    font-size: 27px;
    fill: var(--brand-red);
  }
  .brand-sub {
    font-family: "Poppins", sans-serif;
    font-weight: 700;
    font-size: 19px;
    fill: var(--brand-red);
  }
  .web-address {
    font-family: "Poppins", sans-serif;
    font-weight: 600;
    font-size: 19px;
    letter-spacing: 2.5px;
    fill: var(--ink);
  }
</style>
</head>
<body>
<main class="canvas">

  <!-- Banner A -->
  <svg class="banner banner--plant" viewBox="0 0 415 995" xmlns="http://www.w3.org/2000/svg" aria-label="Pop-up banner, version A">
    <defs>
      <linearGradient id="a-header" x1="0" y1="0" x2="0" y2="1">
        <stop offset="0" stop-color="#232323"/>
        <stop offset="0.55" stop-color="#3a3a3a"/>
        <stop offset="1" stop-color="#050505"/>
      </linearGradient>
      <linearGradient id="a-photo" x1="0" y1="0" x2="0" y2="1">
        <stop offset="0" stop-color="#a9c8e6"/>
        <stop offset="0.3" stop-color="#6f8fb8"/>
        <stop offset="0.6" stop-color="#5d6066"/>
        <stop offset="0.8" stop-color="#d9d9d6"/>
        <stop offset="1" stop-color="#6f9a3c"/>
      </linearGradient>
      <linearGradient id="a-red" x1="0" y1="0" x2="1" y2="1">
        <stop offset="0" stop-color="#7a0d12"/>
        <stop offset="0.6" stop-color="#d6232b"/>
        <stop offset="1" stop-color="#b0141b"/>
      </linearGradient>
      <linearGradient id="a-grey" x1="1" y1="0" x2="0" y2="1">
        <stop offset="0" stop-color="#5e5e5e"/>
        <stop offset="1" stop-color="#b4b4b4"/>
      </linearGradient>
      <linearGradient id="a-pill" x1="0" y1="0" x2="1" y2="0">
        <stop offset="0" stop-color="#ffffff" stop-opacity="0"/>
        <stop offset="0.45" stop-color="#ffffff" stop-opacity="0.9"/>
        <stop offset="1" stop-color="#ffffff"/>
      </linearGradient>
    </defs>

    <rect class="banner-base" x="0" y="0" width="415" height="995" fill="var(--white)"/>

    <g class="photo-main" role="img" aria-label="Photo: excavators demolishing a blue industrial plant building under a blue sky">
      <polygon points="0,215 207,295 415,215 415,615 207,730 0,615" fill="url(#a-photo)"/>
    </g>
    <g class="photo-accent-red" role="img" aria-label="Photo in red tint: heavy equipment on a cleared site">
      <polygon points="0,618 204,732 0,843" fill="url(#a-red)"/>
    </g>
    <g class="photo-accent-grey" role="img" aria-label="Black and white photo: excavator working among rubble">
      <polygon points="415,618 211,732 415,843" fill="url(#a-grey)"/>
    </g>
    <polyline class="photo-divider" points="0,615 207,730 415,615" fill="none" stroke="var(--white)" stroke-width="4"/>

    <g class="header-panel" role="img" aria-label="Dark photo of a cleared industrial site behind the headline">
      <polygon points="0,0 415,0 415,210 207,290 0,210" fill="url(#a-header)"/>
    </g>
    <polyline class="header-edge" points="0,214 207,294 415,214" fill="none" stroke="var(--white)" stroke-width="5"/>

    <text class="tagline-top" x="212" y="70" text-anchor="middle">Building a Nation’s</text>
    <rect class="since-pill" x="204" y="178" width="166" height="30" rx="5" fill="url(#a-pill)"/>
    <text class="since-text" x="360" y="202" text-anchor="end">Since 1968</text>
    <text class="tagline-script" x="200" y="158" text-anchor="middle">Horizon</text>

    <polygon class="footer-panel" points="0,851 207,738 415,851 415,975 0,975" fill="var(--white)"/>
    <polyline class="footer-edge" points="0,847 207,734 415,847" fill="none" stroke="var(--brand-red)" stroke-width="7"/>
    <polygon class="apex-mark" points="207,718 222,729 207,740 192,729" fill="var(--ink)"/>

    <text class="brand-name" x="207" y="855" text-anchor="middle">R.T. HOLLISTER</text>
    <text class="brand-sub" x="207" y="883" text-anchor="middle">Companies</text>

    <text class="web-address" x="207" y="950" text-anchor="middle">www.rthco.com</text>
    <rect class="base-band" x="0" y="975" width="415" height="20" fill="var(--header-black)"/>
  </svg>

  <!-- Banner B -->
  <svg class="banner banner--brewery" viewBox="0 0 415 995" xmlns="http://www.w3.org/2000/svg" aria-label="Pop-up banner, version B">
    <defs>
      <linearGradient id="b-header" x1="0" y1="0" x2="0" y2="1">
        <stop offset="0" stop-color="#262626"/>
        <stop offset="0.55" stop-color="#3d3d3d"/>
        <stop offset="1" stop-color="#060606"/>
      </linearGradient>
      <linearGradient id="b-photo" x1="0" y1="0" x2="0" y2="1">
        <stop offset="0" stop-color="#c9d4de"/>
        <stop offset="0.3" stop-color="#e6d8c4"/>
        <stop offset="0.55" stop-color="#c8412a"/>
        <stop offset="0.78" stop-color="#d9a72a"/>
        <stop offset="1" stop-color="#8d8173"/>
      </linearGradient>
      <linearGradient id="b-red" x1="0" y1="0" x2="1" y2="1">
        <stop offset="0" stop-color="#8a0f14"/>
        <stop offset="0.6" stop-color="#d8242c"/>
        <stop offset="1" stop-color="#b3151c"/>
      </linearGradient>
      <linearGradient id="b-grey" x1="1" y1="0" x2="0" y2="1">
        <stop offset="0" stop-color="#4e4e4e"/>
        <stop offset="1" stop-color="#a8a8a8"/>
      </linearGradient>
      <linearGradient id="b-pill" x1="0" y1="0" x2="1" y2="0">
        <stop offset="0" stop-color="#ffffff" stop-opacity="0"/>
        <stop offset="0.45" stop-color="#ffffff" stop-opacity="0.9"/>
        <stop offset="1" stop-color="#ffffff"/>
      </linearGradient>
    </defs>

    <rect class="banner-base" x="0" y="0" width="415" height="995" fill="var(--white)"/>

    <g class="photo-main" role="img" aria-label="Photo: yellow excavator demolishing a red and tan plant building with tall stacks">
      <polygon points="0,215 207,295 415,215 415,615 207,730 0,615" fill="url(#b-photo)"/>
    </g>
    <g class="photo-accent-red" role="img" aria-label="Photo in red tint: excavator and truck on a job site">
      <polygon points="0,618 204,732 0,843" fill="url(#b-red)"/>
    </g>
    <g class="photo-accent-grey" role="img" aria-label="Black and white photo: industrial structure coming down in a dust cloud">
      <polygon points="415,618 211,732 415,843" fill="url(#b-grey)"/>
    </g>
    <polyline class="photo-divider" points="0,615 207,730 415,615" fill="none" stroke="var(--white)" stroke-width="4"/>

    <g class="header-panel" role="img" aria-label="Dark photo of an industrial plant with a chimney behind the headline">
      <polygon points="0,0 415,0 415,210 207,290 0,210" fill="url(#b-header)"/>
    </g>
    <polyline class="header-edge" points="0,214 207,294 415,214" fill="none" stroke="var(--white)" stroke-width="5"/>

    <text class="tagline-top" x="212" y="70" text-anchor="middle">Building a Nation’s</text>
    <rect class="since-pill" x="204" y="178" width="166" height="30" rx="5" fill="url(#b-pill)"/>
    <text class="since-text" x="360" y="202" text-anchor="end">Since 1968</text>
    <text class="tagline-script" x="200" y="158" text-anchor="middle">Horizon</text>

    <polygon class="footer-panel" points="0,851 207,738 415,851 415,975 0,975" fill="var(--white)"/>
    <polyline class="footer-edge" points="0,847 207,734 415,847" fill="none" stroke="var(--brand-red)" stroke-width="7"/>
    <polygon class="apex-mark" points="207,718 222,729 207,740 192,729" fill="var(--ink)"/>

    <text class="brand-name" x="207" y="855" text-anchor="middle">R.T. HOLLISTER</text>
    <text class="brand-sub" x="207" y="883" text-anchor="middle">Companies</text>

    <text class="web-address" x="207" y="950" text-anchor="middle">www.rthco.com</text>
    <rect class="base-band" x="0" y="975" width="415" height="20" fill="var(--header-black)"/>
  </svg>

</main>
</body>
</html>
```